Modern two-sided business card for a general enterprise that improves the digital user experience.

Our company based in Switzerland covers all services of the digital customer relationship. We automate online ads to acquire new customers and program mobile apps for more efficient customer care in customer service. We employ specialists in marketing, business management, data science, graphic designers, copywriters, UI and programmers. The new business card is intended to show our comprehensive role and various offering of the entire customer journey.

Company Font: Futura
Main Color: # 283583
Secondary: #fcfaee (and gray variations)
Website: https://vko.example

As little address information as possible: company name, employee, mobile, email, company web & company phone.

Target Market(s)

C-Level (CEO, CIO, CTO), Head Sales, Head Marketing & Head Customer Service

Industry/Entity Type

Digital Marketing, Online-Marketing, Analytics

Contact Information for Business Card

Requirements
Must have
• Company logo type ": vko" only on one side

```html
<!DOCTYPE html>
<html lang="en">
<head>
<meta charset="utf-8">
<title>vko – Business Card</title>
<link rel="stylesheet" href="https://fonts.googleapis.com/css2?family=Jost:wght@400;600;700&display=swap">
<style>
  :root {
    --brand-blue: #0010cc;
    --card-grey: #e5e5e5;
    --ink: #111111;
    --paper: #ffffff;
    --text-light: #f0f0f0;
  }
  * { margin: 0; padding: 0; box-sizing: border-box; }
  html, body {
    width: 1200px; height: 1000px; overflow: hidden;
    background: var(--paper);
    font-family: "Jost", "Futura", sans-serif;
  }
  .canvas { position: relative; width: 1200px; height: 1000px; }

  .side-label {
    position: absolute; left: 303px;
    font-size: 31px; font-weight: 400; color: var(--ink);
    line-height: 1;
  }
  .side-label--front { top: 88px; }
  .side-label--back { top: 534px; }

  .card {
    position: absolute; left: 297px;
    width: 606px; height: 346px;
    background: var(--card-grey);
    overflow: hidden;
    box-shadow: 5px 5px 6px rgba(0,0,0,0.35);
  }
  .card--front { top: 127px; }
  .card--back { top: 567px; }

  .contact-band {
    position: absolute; left: 0; top: 0;
    width: 100%; height: 198px;
    background: var(--brand-blue);
    color: var(--text-light);
  }
  .person-name {
    position: absolute; left: 53px; top: 34px;
    font-size: 39px; font-weight: 600; letter-spacing: 0.5px;
    line-height: 1;
  }
  .contact-line {
    position: absolute; display: flex; align-items: center;
    font-size: 27px; font-weight: 400; line-height: 1;
    letter-spacing: 0.3px;
  }
  .contact-line--email { left: 51px; top: 87px; }
  .contact-line--phone { left: 54px; top: 124px; }
  .contact-line svg { flex: none; }
  .contact-line--email svg { margin-right: 14px; }
  .contact-line--phone svg { margin-right: 9px; }

  .company-address {
    position: absolute; left: 0; top: 234px; width: 100%;
    text-align: center; color: var(--brand-blue);
    font-size: 21px; line-height: 30px; letter-spacing: 0.3px;
  }
  .company-address .divider { margin: 0 8px; }

  .company-name {
    position: absolute; left: 0; top: 0; width: 100%; height: 100%;
    display: flex; align-items: center; justify-content: center;
    color: var(--brand-blue);
    font-size: 190px; font-weight: 700; letter-spacing: -4px;
    line-height: 1;
    padding-bottom: 20px;
  }
</style>
</head>
<body>
<div class="canvas">
  <p class="side-label side-label--front">Front</p>
  <section class="card card--front">
    <div class="contact-band">
      <h1 class="person-name">Mara Keller</h1>
      <p class="contact-line contact-line--email">
        <svg width="26" height="16" viewBox="0 0 26 16" fill="none" stroke="currentColor" stroke-width="1.3">
          <rect x="0.7" y="0.7" width="24.6" height="14.6"/>
          <path d="M0.7 0.7 L13 9 L25.3 0.7"/>
          <path d="M0.7 15.3 L10 7.3 M25.3 15.3 L16 7.3"/>
        </svg>
        mara.keller@vko.example
      </p>
      <p class="contact-line contact-line--phone">
        <svg width="22" height="22" viewBox="0 0 24 24" fill="none" stroke="currentColor" stroke-width="1.3" stroke-linejoin="round">
          <path d="M5 2.5 L8.5 6.5 L6.8 9 C8 12 11 15 14 16.5 L16.5 14.8 L20.5 18.3 L18 21.5 C10 20 4 13.5 2.5 5.5 Z"/>
          <path d="M13 5 A6 6 0 0 1 18.5 10.5"/>
          <path d="M13.5 1.5 A9.5 9.5 0 0 1 22 10"/>
        </svg>
        079 555 01 23
      </p>
    </div>
    <address class="company-address" style="font-style: normal;">
      Lindenweg 12<br>
      CH–8000 Musterdorf<br>
      vko.example<span class="divider">|</span>info@vko.example
    </address>
  </section>

  <p class="side-label side-label--back">Back</p>
  <section class="card card--back">
    <p class="company-name">vko</p>
  </section>
</div>
</body>
</html>
```